Ferrant Valley Zoning Council Business Cards

We're looking for a business card design, simple as that. We're a local government agency that mainly performs building code enforcement, transportation planning, floodplain management, and GIS for Tobelle Parish in Louisiana, and other surround parishes. So you're not having to Google anything, GIS is, at it's core, mapping. Building Code Enforcement is just that, nothing more. Floodplain Management is to make sure the public is within what the government

Contact Information for Business Card

Our Address is

517 Marwick Street
Alexandria, LA 71489

Our phone is 3185529137
Our fax is 3185529142
Our website is www.fvzc.info
My email is dana@fvzc.info

Font styles to use
Serif
Sans Serif

Colors

Designer to choose colors to be used in the design.

Requirements
Must have
• I'm attaching our logo(several versions) that must be incorporated. The design should fit well with our existing logo. I can send photoshop files for our logo if needed. If possible, I'd like to be able to add names/info to each card for all of our employees once this is done.
Nice to have
• The Louisiana state seal is a bonus, and isn't specifically required.

```html
<!DOCTYPE html>
<html lang="en">
<head>
<meta charset="utf-8">
<title>Ferrant Valley Zoning Council Business Cards</title>
<link rel="stylesheet" href="https://fonts.googleapis.com/css2?family=Poppins:wght@400;500;600&display=swap">
<style>
  :root {
    --backdrop: #8c8c8c;
    --card-white: #ffffff;
    --panel-black: #050505;
    --brand-green: #1fa61f;
    --brand-lime: #d7f200;
    --brand-blue: #1646d8;
    --brand-orange: #f08a12;
    --ink: #111111;
    --text-light: #f2f2f2;
  }
  html, body {
    margin: 0;
    width: 1200px;
    height: 960px;
    overflow: hidden;
    background: var(--backdrop);
    font-family: "Poppins", sans-serif;
  }
  .card {
    position: absolute;
    width: 752px;
    height: 430px;
    border-radius: 26px;
    overflow: hidden;
    box-shadow: 0 14px 30px rgba(0,0,0,0.35);
  }
  .card-back { left: 60px; top: 40px; }
  .card-front { left: 388px; top: 490px; background: var(--card-white); }

  .pattern-fill {
    width: 100%;
    height: 100%;
    background: linear-gradient(135deg,
      var(--brand-lime) 0%, var(--brand-orange) 28%,
      var(--brand-green) 52%, var(--brand-blue) 76%, var(--brand-orange) 100%);
  }

  .front-graphics { position: absolute; inset: 0; }

  .brand {
    position: absolute;
    left: 64px;
    top: 170px;
    display: flex;
    align-items: center;
    gap: 16px;
  }
  .brand-square {
    width: 58px;
    height: 58px;
    background: var(--brand-green);
    flex: none;
  }
  .brand-name {
    font-weight: 600;
    font-size: 26px;
    line-height: 1.15;
    color: var(--ink);
    width: 300px;
  }

  .contact {
    position: absolute;
    right: 34px;
    top: 42px;
    text-align: right;
    color: var(--text-light);
    font-size: 15px;
    line-height: 1.45;
  }
  .contact-name {
    color: var(--brand-green);
    font-size: 27px;
    font-weight: 500;
    line-height: 1.1;
  }
  .contact-title {
    color: var(--brand-lime);
    font-size: 15px;
    font-weight: 600;
    margin-bottom: 18px;
  }
  .contact-address { margin-bottom: 18px; }
  .contact-line {
    display: flex;
    justify-content: flex-end;
    align-items: center;
    gap: 10px;
  }
  .contact-line svg { width: 14px; height: 14px; flex: none; }
</style>
</head>
<body>

<div class="card card-back">
  <div class="pattern-fill" role="img" aria-label="Honeycomb pattern of hexagon tiles showing map, flood, road sign and building permit icons in green, blue, lime and orange"></div>
</div>

<div class="card card-front">
  <svg class="front-graphics" viewBox="0 0 752 430" aria-hidden="true">
    <polygon points="488,0 752,0 752,430 628,430" fill="var(--panel-black)"/>
    <line x1="452" y1="0" x2="592" y2="430" stroke="var(--brand-blue)" stroke-width="5"/>
    <line x1="464" y1="0" x2="604" y2="430" stroke="var(--brand-orange)" stroke-width="4"/>
    <line x1="476" y1="0" x2="616" y2="430" stroke="var(--brand-lime)" stroke-width="4"/>
  </svg>

  <div class="brand">
    <div class="brand-square"></div>
    <div class="brand-name">Ferrant Valley Zoning Council</div>
  </div>

  <div class="contact">
    <div class="contact-name">Owen Castell</div>
    <div class="contact-title">President</div>
    <div class="contact-address">517 Marwick Street<br>Alexandria, LA 71489</div>
    <div class="contact-line">3185529137
      <svg viewBox="0 0 16 16"><path d="M4 1l3 3-2 2c1 2 3 4 5 5l2-2 3 3-2 3C7 15 1 9 1 3z" fill="var(--brand-green)"/></svg>
    </div>
    <div class="contact-line">3185529142
      <svg viewBox="0 0 16 16"><rect x="4" y="1" width="8" height="5" fill="var(--brand-green)"/><rect x="1" y="6" width="14" height="7" rx="1" fill="var(--brand-green)"/></svg>
    </div>
    <div class="contact-line">dana@fvzc.info
      <svg viewBox="0 0 16 16"><rect x="1" y="3" width="14" height="10" fill="var(--brand-green)"/><path d="M1 3l7 6 7-6" stroke="var(--panel-black)" stroke-width="1.4" fill="none"/></svg>
    </div>
    <div class="contact-line">www.fvzc.info
      <svg viewBox="0 0 16 16"><circle cx="8" cy="8" r="7" fill="var(--brand-green)"/><path d="M1 8h14M8 1c-3 4-3 10 0 14M8 1c3 4 3 10 0 14" stroke="var(--panel-black)" stroke-width="1.2" fill="none"/></svg>
    </div>
  </div>
</div>

</body>
</html>
```